Homebrewing Beer Supplier Needs 2 Product Labels

We have been supplying home wine and beer making supplies through the mail for over 40 years. (website: www.tovalmerch.com) We serve the entire U.S.
We are launching a new line of beer ingredient kits. These are basically boxes of brewing ingredient that have been pre-measured to brew a specific style of beer. One box might contain all the ingredients for brewing an American Lager, another box a Brown Ale, etc. In all, we are starting out with 25 different beers.
We need to have two labels designed:
- The first one is to go on the outside of the box. One single design is needed for all 25 different types of ingredient kits. We will be printing the name of each beer type by laser printer as we use the labels.
-The second label is to go on the jars of malt extract syrup that will be in these beer ingredient kits. We will also be selling these jars of malt extract syrup separately, as a stand-alone products.
Target Market(s)
These labels should appeal to homebrewers. There typical age range is 25 to 40. Mostly male with a deep appreciation for beer.
Requirements
Must have
- The brand name for both of these labels is Gilded Rattle. Since this is a new brand there is no logo, so you'll need to come up with something to go on the labels. Both labels should have the same style and/or theme.
The idea behind the name Gilded Rattle was to build imagery off of the steam age/steam punk/industrial revolution: Not steam trains necessarily, but think along the line of: cog wheels, springs, pressure gauges, goggles, contraptions, concoctions,Victorian, brass, brick, cast-iron, etc.
- Ingredient Kit Label:
The dimensions of the beer ingredient kit label to go on the outside of the box is 8.4375" wide and 5.4375" tall. No bleeds. The only verbiage it has to have is the brand, "Gilded Rattle" with a tag line "Beer Ingredient Kits". It would also need have "Makes 5 Gallons" or something similar somewhere on the label. More verbiage is acceptable if your design needs it.
There also needs to be a space for us to laser print the type of beer it is making as we use the labels. This area needs to be about 4.5" wide and .75" tall. You can re-size the laser printing area to be bigger or smaller as needed. Just keep the ratio of width-to-height about the same. Also keep the laser print area at least .25" or more away from the labels edge.
Find attached this project a picture the panel-side of the box where the label is to be places.
- Malt Extract Syrup Label:
On this label you have a choice of two sizes. Use whichever size works best. The first size is 3.75" tall and 4.5" wide. The second label size is 3.75" tall and 6" wide. The total circumference of the jar is 12", so the larger label would go half way around it. Either label size will have rounded corners with a radius of .125". Bleeds are allowed on these jar labels.
You can find a picture of the jar attached to this project. The malt extract syrup going into the jar will vary some in color. The color range can be found in the third picture attached.
There are 5 different flavors of malt syrup, so I will need 5 different versions of this jar label. The design of the label is the same on each version. It is only some of the wording that is changing. All of the versions of this label will need:
Gilded Rattle
Net Wt. 3.3 lbs. (1.5 kg.)
Packaged By:
R. J. Pellow
418 W. Harlan Ave.
Independence, MO 64053
1-800-555-0147
Website: www.TOValmerch.com
-
Below is the wording changes for each version.
-
Version #1:
Light
Ingredients:
100% Pure Malt Extract (Base Malt, Dunvoro® Malt, Water)
Analysis:
Approx. 80% Malt Solids
Color: 4° Lovibond
Reorder No: GRT120
-
Version #2:
Amber
Ingredients:
100% Pure Malt Extract (Malted Barley, Water)
Analysis:
Approx. 80% Malt Solids
Color: 10° Lovibond
Reorder No: GRT140
-
Version #3:
Wheat
Ingredients:
100% Pure Malt Extract (Wheat Malt, Base Malt, Water)
Analysis:
Approx. 80% Malt Solids
Color: 3° Lovibond
Reorder No: GRT110
-
Version #4:
Dark
Ingredients:
100% Pure Malt Extract (Munich Malt, Base Malt, Caramel Malt 60°L, Water)
Analysis:
Approx. 80% Malt Solids
Color: 30° Lovibond
Reorder No: GRT150
-
Version #4:
Munich
Ingredients:
100% Pure Malt Extract (Barley Malt, Water)
Analysis:
Approx. 80% Malt Solids
Color: 8° Lovibond
Reorder No: GRT130

```html
<!DOCTYPE html>
<html lang="en">
<head>
<meta charset="utf-8">
<title>Gilded Rattle – Beer Ingredient Kit Label</title>
<link rel="stylesheet" href="https://fonts.googleapis.com/css2?family=Source+Sans+3:wght@400;700;900&family=Caveat:wght@500&display=swap">
<style>
  :root {
    --page: #ffffff;
    --kraft: #f4d4ab;
    --kraft-light: #f6dcb8;
    --ink: #0d0b0a;
    --ink-soft: #2e2926;
    --ring: #7a716a;
    --cream: #f5e6cc;
    --print-area: #f7efe6;
  }
  * { margin: 0; padding: 0; box-sizing: border-box; }
  html, body {
    width: 1200px;
    height: 555px;
    overflow: hidden;
    background: var(--page);
  }
  .canvas {
    width: 1200px;
    height: 555px;
    display: flex;
    align-items: center;
    justify-content: center;
  }
  .kit-label {
    display: block;
    width: 840px;
    height: 539px;
  }
  .seal-outer { fill: var(--ink-soft); stroke: var(--kraft-light); stroke-width: 5; }
  .seal-inner { fill: var(--ink); stroke: var(--ring); stroke-width: 9; }
  .diagonal-band { fill: var(--ink); }
  .seal-banner { fill: var(--ink); stroke: var(--ring); stroke-width: 3; }
  .seal-star { fill: var(--ring); }
  .seal-star.is-main { fill: var(--cream); }
  .brand-name {
    font-family: "Source Sans 3", sans-serif;
    font-weight: 900;
    fill: var(--cream);
  }
  .style-word {
    font-family: "Source Sans 3", sans-serif;
    font-weight: 900;
    fill: var(--cream);
    letter-spacing: 2px;
  }
  .yield-note {
    font-family: "Source Sans 3", sans-serif;
    font-weight: 400;
    fill: var(--cream);
    letter-spacing: 1px;
  }
  .tagline {
    font-family: "Caveat", cursive;
    font-weight: 500;
    fill: var(--ink);
  }
  .badge-outer { fill: var(--ink); }
  .badge-ring { fill: none; stroke: var(--cream); stroke-width: 8; }
  .print-area { fill: var(--print-area); }
</style>
</head>
<body>
<main class="canvas">
  <svg class="kit-label" viewBox="0 0 912 585" xmlns="http://www.w3.org/2000/svg" aria-label="Gilded Rattle beer ingredient kit label">
    <defs>
      <clipPath id="seal-clip">
        <ellipse cx="250" cy="290" rx="216" ry="279"/>
      </clipPath>
      <linearGradient id="kraft-tone" x1="0" y1="0" x2="1" y2="0">
        <stop offset="0" stop-color="#f5d7b0"/>
        <stop offset="1" stop-color="#f1cfa3"/>
      </linearGradient>
    </defs>

    <rect class="label-ground" x="0" y="0" width="912" height="585" fill="url(#kraft-tone)" role="img" aria-label="Kraft paper background with fine vertical pinstripes"/>

    <polygon class="diagonal-band" points="0,296 910,16 910,158 0,448"/>

    <g class="seal">
      <ellipse class="seal-outer" cx="250" cy="290" rx="216" ry="279" role="img" aria-label="Dark oval seal with diagonal pinstripe texture"/>
      <ellipse class="seal-inner" cx="258" cy="316" rx="134" ry="190"/>
      <g clip-path="url(#seal-clip)">
        <polygon class="seal-banner" points="-10,299 520,136 520,288 -10,451"/>
      </g>

      <g class="seal-stars">
        <polygon class="seal-star" points="218,163 221,168 227,169 222,173 224,179 218,176 212,179 214,173 209,169 215,168"/>
        <polygon class="seal-star is-main" points="258,156 262,165 272,166 265,172 267,182 258,177 249,182 251,172 244,166 254,165"/>
        <polygon class="seal-star" points="296,163 299,168 305,169 300,173 302,179 296,176 290,179 292,173 287,169 293,168"/>
      </g>

      <g transform="rotate(-16 262 320)">
        <text class="brand-name" x="318" y="262" font-size="54" text-anchor="middle">Gilded</text>
        <text class="brand-name" x="258" y="352" font-size="100" text-anchor="middle">Rattle</text>
      </g>

      <text class="style-word" x="272" y="428" font-size="42" text-anchor="middle">BEER</text>
    </g>

    <text class="yield-note" x="678" y="175" font-size="38" text-anchor="middle" transform="rotate(-17 678 163)">Makes 5 Gallons</text>

    <text class="tagline" x="688" y="300" font-size="58" text-anchor="middle" transform="rotate(-15 688 283)">Beer Ingredient Kits</text>

    <g class="quality-badge">
      <circle class="badge-outer" cx="803" cy="395" r="68"/>
      <circle class="badge-ring" cx="803" cy="395" r="52"/>
    </g>

    <rect class="print-area" x="456" y="482" width="426" height="72" aria-label="Space for printed beer style"/>
  </svg>
</main>
</body>
</html>
```